Website for enterprise software start-up

We need a new Wordpress website. We are an early stage start-up focused on mobile video technology for cellular operators. The audience is strategy, marketing and customer acquisition execs from the operators.

The purpose of the site is to act as a sales brochure and capture leads. A demo app can be downloaded from the current site, want to put that behind a contact form.

Current website is at www.brellowmo.tv. Similar number of pages. Looking for a clean design template, with minimal customization. Blog will remain as is.

Want to be able to modify the copy via Wordpress. Reference designs I like: vandrisk.com, tallowquarrymetric.com

Target Market(s)

Mobile operators and MVNOs in the US and Asia Pacific regions

Industry/Entity Type

Business Software

Coding

Coded - Design and coding required

Number of Pages Required

4 page

Font styles to use
Sans Serif

Colors
f78f20

Requirements
Must have
• Form for downloading sample apps.
• Landing page with image, Product, Blog, About, Contact
• Team page

```html
<!DOCTYPE html>
<html lang="en">
<head>
<meta charset="utf-8">
<title>Brellowmo Media — Mobile Video Engagement</title>
<link rel="stylesheet" href="https://fonts.googleapis.com/css2?family=Montserrat:wght@400;600;700&family=Open+Sans:wght@400;600;700&display=swap">
<style>
:root{
  --orange:#f78f20;
  --orange-dark:#e57d10;
  --ink:#333333;
  --muted:#777777;
  --light:#f2f2f2;
  --line:#dddddd;
  --dark:#2b2b2b;
  --white:#ffffff;
  --screen-top:#2c3e5e;
  --screen-bottom:#7f9cc4;
  --bezel:#1c1c1c;
}
*{box-sizing:border-box;margin:0;padding:0}
html,body{width:1200px;height:3724px;overflow:hidden}
body{font-family:"Open Sans",Arial,sans-serif;color:var(--ink);background:var(--white);position:relative}
h1,h2,h3,.brand,.btn,.nav a{font-family:"Montserrat",Arial,sans-serif}
section,header,footer{position:absolute;left:0;width:1200px}
.section-title{text-align:center;font-size:34px;font-weight:700;color:var(--ink);letter-spacing:.5px}
.section-title.orange{color:var(--orange)}
.title-rule{display:block;width:60px;height:3px;background:var(--orange);margin:12px auto 0}
.btn{display:inline-block;font-size:12px;font-weight:700;text-transform:uppercase;border-radius:3px;padding:8px 16px;letter-spacing:.5px;white-space:nowrap}
.btn-orange{background:var(--orange);color:var(--white)}
.btn-dark{background:var(--dark);color:var(--white)}
.btn-white{background:var(--white);color:var(--ink)}

/* Hero */
.hero{top:0;height:560px;background:linear-gradient(100deg,#3a3a3a 0%,#5c5c5c 45%,#8a8a8a 70%,#4a4a4a 100%)}
.hero-photo{position:absolute;inset:0;background:radial-gradient(ellipse at 80% 60%,rgba(215,200,185,.55),rgba(0,0,0,0) 45%),radial-gradient(ellipse at 30% 40%,rgba(255,255,255,.12),rgba(0,0,0,0) 50%)}
.topbar{position:absolute;top:0;left:0;width:1200px;height:56px;display:flex;align-items:center;justify-content:space-between;padding:0 40px;background:rgba(255,255,255,.92)}
.nav{display:flex;gap:22px;width:260px}
.nav a{font-size:12px;font-weight:700;color:var(--ink);text-decoration:none}
.brand{display:flex;align-items:center;gap:8px;font-size:24px;font-weight:700;color:var(--ink)}
.brand-square{width:22px;height:22px;background:var(--orange);border-radius:3px}
.top-actions{display:flex;gap:10px;width:260px;justify-content:flex-end}
.hero-content{position:absolute;top:260px;left:0;width:1200px;text-align:center;color:var(--white)}
.play-ring{width:80px;height:80px;margin:0 auto 26px;display:block}
.hero h1{font-size:40px;font-weight:700;letter-spacing:.5px}
.hero p{font-size:16px;margin:12px 0 26px;color:#eeeeee}

/* Push video */
.push{top:560px;height:820px;background:var(--white)}
.push-head{position:absolute;top:70px;width:1200px}
.push-sub{text-align:center;font-size:16px;color:var(--muted);margin-top:6px;font-style:italic}
.features{position:absolute;top:200px;left:120px;width:480px}
.feature{position:relative;height:116px;text-align:right;padding-right:86px;padding-top:6px}
.feature h3{font-family:"Open Sans",Arial,sans-serif;font-size:15px;font-weight:700;color:var(--ink);margin-bottom:4px}
.feature p{font-size:12px;color:var(--muted);line-height:1.45}
.feature-icon{position:absolute;right:0;top:0;width:56px;height:56px;border-radius:50%;background:var(--orange);display:flex;align-items:center;justify-content:center}
.feature-icon svg{width:26px;height:26px}
.feature-links{position:absolute;top:228px;left:600px}
.hand-phone{position:absolute;top:170px;left:700px;width:320px;height:600px;border-radius:40px 40px 0 0;background:linear-gradient(180deg,rgba(0,0,0,0) 70%,#e6cdb6 100%),#f4f4f4;border:1px solid #e2e2e2}
.hand-phone-screen{position:absolute;top:70px;left:20px;width:278px;height:440px;border-radius:4px;background:linear-gradient(180deg,var(--screen-top) 0%,#4c638a 45%,var(--screen-bottom) 100%)}
.hand-phone-speaker{position:absolute;top:34px;left:130px;width:60px;height:6px;border-radius:3px;background:#cfcfcf}

/* Products */
.products{top:1380px;height:580px;background:linear-gradient(180deg,#ededed,#f7f7f7)}
.products .section-title{padding-top:50px}
.carousel{position:absolute;top:150px;left:0;width:1200px;height:300px}
.arrow{position:absolute;width:34px;height:34px;border-radius:50%;background:var(--dark);display:flex;align-items:center;justify-content:center}
.arrow svg{width:12px;height:12px}
.carousel .arrow{top:130px}
.arrow.left{left:40px}.arrow.right{right:40px}
.device{position:absolute;border-radius:14px;background:var(--bezel);padding:14px 6px 18px}
.device .screen{width:100%;height:100%;border-radius:2px;background:linear-gradient(180deg,var(--screen-top),var(--screen-bottom))}
.device.side{opacity:.75}
.device.side .screen{background:linear-gradient(180deg,#5a5a5a,#a9a9a9)}
.device.main .screen{background:linear-gradient(180deg,#1e2b44 0%,#3a5580 50%,#c8792c 100%)}
.device-label{position:absolute;font-family:"Montserrat",Arial,sans-serif;font-size:11px;font-weight:700;color:var(--ink);text-align:center;width:140px;line-height:1.3}
.mini-brand{display:flex;align-items:center;justify-content:center;gap:4px;font-family:"Montserrat",Arial,sans-serif;font-size:11px;font-weight:700;color:var(--ink);margin-bottom:3px}
.mini-brand i{display:block;width:9px;height:9px;background:var(--orange);border-radius:2px}
.store-row{position:absolute;top:460px;left:0;width:1200px;display:flex;justify-content:center;align-items:center;gap:60px}
.store-badge{display:block;width:200px;height:60px;border-radius:10px;background:linear-gradient(180deg,#2a2a2a,#050505);border:1px solid #6a6a6a}
.showcase{text-align:center}
.showcase .mini-brand{font-size:16px}
.showcase .mini-brand i{width:14px;height:14px}
.showcase-label{font-family:"Montserrat",Arial,sans-serif;font-size:18px;font-weight:700;color:var(--orange)}

/* Blog */
.blog{top:1960px;height:480px;background:var(--white)}
.blog .section-title{padding-top:40px}
.blog-grid{position:absolute;top:130px;left:130px;display:flex;gap:34px}
.post{width:210px}
.post-image{height:165px;background:linear-gradient(160deg,#7a6a58,#c9a070 60%,#4e5560)}
.post-image.sky{background:linear-gradient(180deg,#d9b58a,#b57d4c 60%,#3d3f45)}
.post h3{font-size:12px;font-weight:700;color:var(--orange);margin:12px 0 4px;text-transform:uppercase;line-height:1.3}
.post .meta{font-size:11px;color:var(--muted);margin-bottom:6px}
.post p{font-size:11px;color:var(--muted);line-height:1.45;margin-bottom:10px}

/* Team */
.team{top:2440px;height:460px;background:var(--orange)}
.team .section-title{color:var(--white);padding-top:40px}
.team .title-rule{background:var(--white)}
.team-row{position:absolute;top:120px;left:130px;display:flex;gap:42px}
.member{width:152px;height:280px;background:var(--white);border-radius:4px;text-align:center;padding-top:22px}
.member-photo{width:104px;height:104px;border-radius:50%;margin:0 auto;background:linear-gradient(180deg,#c8c8c8,#8e8e8e);border:4px solid var(--light)}
.member h3{font-size:13px;font-weight:700;margin-top:16px}
.member .role{font-size:11px;color:var(--muted);margin:3px 0 12px}
.socials{display:flex;justify-content:center;gap:6px}
.social{width:20px;height:20px;border-radius:50%;background:#555}
.team .arrow{top:230px;background:rgba(255,255,255,.35)}

/* About */
.about{top:2900px;height:300px;background:var(--white)}
.about .section-title{padding-top:40px}
.about p{position:absolute;top:130px;left:180px;width:840px;text-align:center;font-size:12px;color:var(--muted);line-height:1.6}
.partners{position:absolute;top:220px;left:0;width:1200px;display:flex;justify-content:center;align-items:center;gap:64px}
.partner{font-family:"Open Sans",Arial,sans-serif;font-size:18px;font-weight:700;color:#555}

/* Contact */
.contact{top:3200px;height:320px;background:var(--light)}
.contact .section-title{padding-top:36px}
.contact-form{position:absolute;top:130px;left:180px;width:840px;display:grid;grid-template-columns:1fr 1fr;gap:20px}
.field{height:34px;background:var(--white);border:1px solid var(--line);font-size:11px;color:#999;padding:10px}
.field-pair{display:grid;grid-template-columns:1fr 1fr;gap:10px}
.col{display:flex;flex-direction:column;gap:10px}
.message{height:78px}
.form-foot{display:flex;align-items:center;justify-content:space-between;font-size:12px;color:var(--ink)}
.radio{display:inline-block;width:11px;height:11px;border-radius:50%;border:1px solid #999;background:var(--white);vertical-align:middle;margin:0 4px 0 10px}
.radio.on{background:var(--orange);border-color:var(--orange)}

/* Footer */
.footer-stores{top:3520px;height:152px;background:#dcdcdc;display:flex;justify-content:center;align-items:center;gap:26px}
.footer-stores .store-badge{width:170px;height:52px}
.bottombar{top:3672px;height:52px;background:var(--white);display:flex;align-items:center;justify-content:space-between;padding:0 40px;font-size:11px;color:var(--muted)}
.bottombar .socials .social{background:#888}
</style>
</head>
<body>

<header class="hero">
  <div class="hero-photo" role="img" aria-label="Photo of a person holding a smartphone, softly blurred in dark grey tones"></div>
  <div class="topbar">
    <nav class="nav"><a>PRODUCT</a><a>BLOG</a><a>ABOUT</a><a>CONTACT</a></nav>
    <div class="brand"><span class="brand-square"></span>Brellowmo</div>
    <div class="top-actions"><span class="btn btn-orange">Login</span><span class="btn btn-white">Sample Apps</span></div>
  </div>
  <div class="hero-content">
    <svg class="play-ring" viewBox="0 0 80 80"><circle cx="40" cy="40" r="36" fill="none" stroke="#f78f20" stroke-width="3"/><path d="M32 26 L56 40 L32 54 Z" fill="#f78f20"/></svg>
    <h1>HIGH QUALITY MOBILE ENGAGEMENT</h1>
    <p>We engage mobile audiences with the right video content at the perfect moment.</p>
    <span class="btn btn-dark">&#9656; Sample Apps</span>
  </div>
</header>

<section class="push">
  <div class="push-head">
    <h2 class="section-title orange">PUSH VIDEO NOTIFICATIONS</h2>
    <div class="push-sub">- at your fingertips</div>
  </div>
  <div class="features">
    <div class="feature"><h3>Reach your mobile audience</h3><p>with beautiful HD thumbnails and in notification videos</p>
      <span class="feature-icon"><svg viewBox="0 0 24 24"><rect x="7" y="2" width="10" height="20" rx="2" fill="none" stroke="#fff" stroke-width="2"/><circle cx="12" cy="18" r="1.2" fill="#fff"/></svg></span></div>
    <div class="feature"><h3>Instant video playback, zero buffering,</h3><p>guaranteed flawless playback - even when offline</p>
      <span class="feature-icon"><svg viewBox="0 0 24 24"><path d="M8 5 L19 12 L8 19 Z" fill="#fff"/></svg></span></div>
    <div class="feature"><h3>Content is personalised based</h3><p>on viewer interests and mobile viewing habits</p>
      <span class="feature-icon"><svg viewBox="0 0 24 24"><circle cx="12" cy="8" r="4" fill="#fff"/><path d="M4 21 C4 15 20 15 20 21 Z" fill="#fff"/></svg></span></div>
    <div class="feature"><h3>Monetize with</h3><p>beautiful HD pre-roll or interstitial ads</p>
      <span class="feature-icon"><svg viewBox="0 0 24 24"><circle cx="12" cy="12" r="9" fill="none" stroke="#fff" stroke-width="2"/><path d="M12 6 V18 M15 9 H10.5 a1.8 1.8 0 0 0 0 3.6 h3 a1.8 1.8 0 0 1 0 3.6 H9" fill="none" stroke="#fff" stroke-width="1.6"/></svg></span></div>
    <div class="feature"><h3>Easily added to</h3><p>your existing apps within one hour</p>
      <span class="feature-icon"><svg viewBox="0 0 24 24"><path d="M12 5 V19 M5 12 H19" stroke="#fff" stroke-width="2.6" stroke-linecap="round"/></svg></span></div>
  </div>
  <svg class="feature-links" width="120" height="470" viewBox="0 0 120 470">
    <path d="M0 0 H110 M0 116 H110 M0 232 H110 M0 348 H110 M0 464 H110" fill="none" stroke="#f78f20" stroke-width="2" stroke-dasharray="4 5"/>
  </svg>
  <div class="hand-phone" role="img" aria-label="Hand holding a white smartphone showing video notification thumbnails">
    <span class="hand-phone-speaker"></span>
    <span class="hand-phone-screen"></span>
  </div>
</section>

<section class="products">
  <h2 class="section-title">OUR PRODUCTS</h2>
  <span class="title-rule"></span>
  <div class="carousel">
    <span class="arrow left"><svg viewBox="0 0 12 12"><path d="M8 1 L3 6 L8 11" fill="none" stroke="#fff" stroke-width="2"/></svg></span>
    <span class="arrow right"><svg viewBox="0 0 12 12"><path d="M4 1 L9 6 L4 11" fill="none" stroke="#fff" stroke-width="2"/></svg></span>
    <div class="device side" style="left:135px;top:60px;width:80px;height:150px" role="img" aria-label="Phone screen showing an app preview"><div class="screen"></div></div>
    <div class="device-label" style="left:250px;top:-6px"><div class="mini-brand"><i></i>Brellowmo</div>NATIVE PUSH VIDEO</div>
    <div class="device" style="left:270px;top:34px;width:100px;height:190px" role="img" aria-label="Phone screen showing native push video"><div class="screen"></div></div>
    <div class="device main" style="left:500px;top:0;width:200px;height:290px" role="img" aria-label="Phone screen showing a video showcase player"><div class="screen"></div></div>
    <div class="device-label" style="left:760px;top:-18px"><div class="mini-brand"><i></i>Brellowmo</div>PUSH VIDEO<br>NOTIFICATIONS</div>
    <div class="device" style="left:780px;top:34px;width:100px;height:190px" role="img" aria-label="Phone screen showing push video notifications"><div class="screen"></div></div>
    <div class="device side" style="left:985px;top:60px;width:80px;height:150px" role="img" aria-label="Phone screen showing an app preview"><div class="screen"></div></div>
  </div>
  <div class="store-row">
    <span class="store-badge" role="img" aria-label="App store download badge"></span>
    <div class="showcase"><div class="mini-brand"><i></i>Brellowmo</div><span class="showcase-label">PUSH VIDEO SHOWCASE</span></div>
    <span class="store-badge" role="img" aria-label="Play store download badge"></span>
  </div>
</section>

<section class="blog">
  <h2 class="section-title">LATEST BLOG</h2>
  <span class="title-rule"></span>
  <div class="blog-grid">
    <article class="post"><div class="post-image" role="img" aria-label="Vintage television set on a wooden shelf"></div><h3>Operators turn to push video for engagement</h3><div class="meta">June 20, 2015 / Arlo Denner</div><p>Short mobile clips keep subscribers coming back and lift daily usage.</p><span class="btn btn-dark">Read More</span></article>
    <article class="post"><div class="post-image sky" role="img" aria-label="Hand holding a phone against a sunset sky"></div><h3>Operators turn to push video for engagement</h3><div class="meta">June 20, 2015 / Arlo Denner</div><p>Short mobile clips keep subscribers coming back and lift daily usage.</p><span class="btn btn-dark">Read More</span></article>
    <article class="post"><div class="post-image" role="img" aria-label="Vintage television set on a wooden shelf"></div><h3>Operators turn to push video for engagement</h3><div class="meta">June 20, 2015 / Arlo Denner</div><p>Short mobile clips keep subscribers coming back and lift daily usage.</p><span class="btn btn-dark">Read More</span></article>
    <article class="post"><div class="post-image sky" role="img" aria-label="Hand holding a phone against a sunset sky"></div><h3>Operators turn to push video for engagement</h3><div class="meta">June 20, 2015 / Arlo Denner</div><p>Short mobile clips keep subscribers coming back and lift daily usage.</p><span class="btn btn-dark">Read More</span></article>
  </div>
</section>

<section class="team">
  <h2 class="section-title">MANAGEMENT TEAM</h2>
  <span class="title-rule"></span>
  <span class="arrow left"><svg viewBox="0 0 12 12"><path d="M8 1 L3 6 L8 11" fill="none" stroke="#fff" stroke-width="2"/></svg></span>
  <span class="arrow right"><svg viewBox="0 0 12 12"><path d="M4 1 L9 6 L4 11" fill="none" stroke="#fff" stroke-width="2"/></svg></span>
  <div class="team-row">
    <div class="member"><div class="member-photo" role="img" aria-label="Portrait of team member"></div><h3>ARLO DENNER</h3><div class="role">CEO</div><div class="socials"><span class="social"></span><span class="social"></span><span class="social"></span></div></div>
    <div class="member"><div class="member-photo" role="img" aria-label="Portrait of team member"></div><h3>TORIN VASQUELL</h3><div class="role">CTO</div><div class="socials"><span class="social"></span><span class="social"></span><span class="social"></span></div></div>
    <div class="member"><div class="member-photo" role="img" aria-label="Portrait of team member"></div><h3>EMMET KRAULD</h3><div class="role">CFO</div><div class="socials"><span class="social"></span><span class="social"></span><span class="social"></span></div></div>
    <div class="member"><div class="member-photo" role="img" aria-label="Portrait of team member"></div><h3>ARLO DENNER</h3><div class="role">CEO</div><div class="socials"><span class="social"></span><span class="social"></span><span class="social"></span></div></div>
    <div class="member"><div class="member-photo" role="img" aria-label="Portrait of team member"></div><h3>ARLO DENNER</h3><div class="role">CEO</div><div class="socials"><span class="social"></span><span class="social"></span><span class="social"></span></div></div>
  </div>
</section>

<section class="about">
  <h2 class="section-title">ABOUT BRELLOWMO MEDIA</h2>
  <span class="title-rule"></span>
  <p>Brellowmo Media builds push video technology for mobile operators. Subscribers receive short, personalised clips in rich notifications that play instantly, even offline. Our platform helps operators lift engagement, cut churn and open new revenue from premium video advertising across every handset on their network.</p>
  <div class="partners">
    <span class="partner">Lumacast</span><span class="partner">Veranta</span><span class="partner">Hollis Arena</span><span class="partner">Tarvel</span><span class="partner">Kestrel TV</span>
  </div>
</section>

<section class="contact">
  <h2 class="section-title">CONTACT US</h2>
  <span class="title-rule"></span>
  <div class="contact-form">
    <div class="col">
      <div class="field-pair"><div class="field">First Name</div><div class="field">Last Name</div></div>
      <div class="field">Subject</div>
      <div class="field">Email Address</div>
    </div>
    <div class="col">
      <div class="field message">Message</div>
      <div class="form-foot"><span>Subscribe to mailing list<span class="radio on"></span>Yes<span class="radio"></span>No</span><span class="btn btn-orange">Submit Now</span></div>
    </div>
  </div>
</section>

<footer class="footer-stores">
  <span class="store-badge" role="img" aria-label="App store download badge"></span>
  <span class="store-badge" role="img" aria-label="Play store download badge"></span>
  <span class="store-badge" role="img" aria-label="Certified developer partner badge"></span>
</footer>
<footer class="bottombar">
  <span>© 2015 BRELLOWMO MEDIA, INC. &nbsp; PRIVACY POLICY</span>
  <div class="socials"><span class="social"></span><span class="social"></span><span class="social"></span></div>
</footer>

</body>
</html>
```